New company branded Power Point Template for presentations

We would like to have a clean and professional PowerPoint template made for our rebranding effort. It will be for our main company (Kelvanorix) and will be used for both general introductory presentations and more technical industry related webinar and in-person presentations. We are a company in the manufacturing space working primarily in automotive. We provide simulation services to optimize production and softwares to allow users to do the same for themselves. The template needs to be easy to modify (even for novice users). I would like a good cover slide, content slides with common title / logo / etc. and a Q&A slide along with a final slide "Thank you" of similar. I have included our brand style guide in a high res pdf. Its images should be sufficient but please let me know if that is not the case.

```html
<!DOCTYPE html>
<html lang="en">
<head>
<meta charset="utf-8">
<title>Kelvanorix Presentation Template</title>
<link rel="stylesheet" href="https://fonts.googleapis.com/css2?family=Barlow+Condensed:wght@600;700&family=Montserrat:wght@400;500;600;700&display=swap">
<style>
:root{
  --navy:#0d2a4c;
  --navy-deep:#0a2240;
  --teal:#1a8aa8;
  --orange:#f39a12;
  --ink:#222831;
  --muted:#6d737b;
  --canvas:#e9e9e9;
  --grid:#e2e4e8;
  --white:#ffffff;
}
*{box-sizing:border-box;margin:0;padding:0}
html,body{width:1200px;height:5296px;overflow:hidden;background:var(--canvas)}
body{font-family:"Montserrat",sans-serif;color:var(--ink);position:relative}
.slide{position:absolute;left:60px;width:1080px;height:608px;background:var(--white);overflow:hidden;box-shadow:0 1px 4px rgba(0,0,0,.12)}
.slide--dark{background:var(--navy)}

/* header */
.slide-header{position:absolute;left:0;top:0;width:1080px;height:80px}
.slide-title{position:absolute;left:47px;top:12px;font-family:"Barlow Condensed",sans-serif;font-weight:700;font-size:33px;letter-spacing:.5px;color:var(--white);text-transform:uppercase}

/* footer */
.slide-footer{position:absolute;left:0;top:580px;width:1080px;height:28px}
.footer-page,.footer-copy{position:absolute;top:585px;font-size:9px;font-weight:600;color:var(--white)}
.footer-page{left:47px}
.footer-copy{left:450px;font-weight:500}
.brand{position:absolute;display:flex;align-items:center;gap:6px;font-family:"Montserrat",sans-serif;font-weight:700;letter-spacing:1px;text-transform:uppercase}
.brand-square{display:block;background:var(--teal)}
.brand--footer{left:920px;top:577px;font-size:10px;color:var(--navy)}
.brand--footer .brand-square{width:18px;height:18px}

/* cover */
.cover-bg{position:absolute;inset:0;background:linear-gradient(105deg,#0d2a4c 0%,#14355d 45%,#1f4d7a 70%,#173d66 100%)}
.cover-shape{position:absolute;right:0;top:0;width:420px;height:608px}
.brand--cover{left:45px;top:40px;font-size:21px;color:var(--white)}
.brand--cover .brand-square{width:40px;height:40px;background:var(--orange)}
.cover-kicker{position:absolute;left:47px;top:200px;font-size:15px;font-weight:700;color:var(--orange);text-transform:uppercase}
.cover-title{position:absolute;left:45px;top:224px;font-family:"Barlow Condensed",sans-serif;font-weight:700;font-size:84px;color:var(--white);line-height:1}
.cover-sub{position:absolute;left:47px;top:331px;font-size:20px;font-weight:500;line-height:33px;color:var(--white)}
.cover-date{position:absolute;left:47px;top:429px;width:202px;height:58px;border-radius:14px 14px 14px 0;background:var(--orange);color:var(--navy);font-size:18px;font-weight:600;display:flex;align-items:center;justify-content:center}

/* about */
.about-lead{position:absolute;left:47px;top:154px;width:430px;font-family:"Barlow Condensed",sans-serif;font-weight:700;font-size:17px;line-height:28px;color:var(--navy);text-transform:uppercase}
.about-body{position:absolute;left:47px;top:216px;width:430px;font-size:13px;line-height:24px;color:var(--muted)}
.about-body p+p{margin-top:6px}
.about-photo{position:absolute;left:551px;top:125px;width:479px;height:412px;border-radius:0 48px 0 48px;background:linear-gradient(120deg,#c99a1e 0%,#6c6134 30%,#2d3c4f 60%,#5c7886 100%)}

/* chart */
.chart{position:absolute;left:40px;top:125px;width:630px;height:400px}
.chart text{font-family:"Montserrat",sans-serif;font-size:11px;fill:var(--ink)}
.tick-list{position:absolute;left:732px;top:136px;width:300px;list-style:none}
.tick-list li{position:relative;padding-left:26px;font-size:11.5px;line-height:21px;color:var(--muted);margin-bottom:10px}
.tick-list svg{position:absolute;left:0;top:4px;width:13px;height:13px}

/* services */
.service-card{position:absolute;top:130px;width:308px;height:398px;background:var(--white);box-shadow:0 3px 10px rgba(0,0,0,.12);text-align:center}
.service-photo{height:214px}
.service-kicker{margin-top:22px;font-size:12px;font-weight:600;color:var(--orange);text-transform:uppercase}
.service-name{margin-top:10px;font-family:"Barlow Condensed",sans-serif;font-weight:700;font-size:18px;color:var(--navy);text-transform:uppercase}
.service-text{margin:8px 24px 0;font-size:11.5px;line-height:20px;color:var(--muted)}

/* team */
.member{position:absolute;background:var(--white);box-shadow:0 3px 10px rgba(0,0,0,.1)}
.member--top{top:158px;width:314px;height:196px;text-align:center}
.member--wide{top:387px;width:442px;height:154px}
.avatar{position:absolute;border-radius:50%;border:3px solid var(--white);box-shadow:0 2px 6px rgba(0,0,0,.2);background:linear-gradient(160deg,#7a8a99,#3e4b59)}
.member-name{font-family:"Barlow Condensed",sans-serif;font-weight:700;font-size:15px;color:var(--navy);text-transform:uppercase}
.member-role{font-size:10px;color:var(--teal);margin-top:2px}
.member-text{font-size:11.5px;line-height:23px;color:var(--muted);margin-top:4px}

/* q&a */
.qa-art{position:absolute;left:345px;top:160px;width:392px;height:268px;border-radius:130px;background:linear-gradient(90deg,var(--navy) 0%,var(--navy) 40%,var(--teal) 62%,var(--teal) 100%)}

/* thank you */
.brand--thanks{left:0;right:0;top:210px;flex-direction:column;gap:14px;font-size:30px;color:var(--white);letter-spacing:3px}
.brand--thanks .brand-square{width:80px;height:80px;background:var(--teal)}
.thanks-title{position:absolute;left:0;right:0;top:362px;text-align:center;font-family:"Barlow Condensed",sans-serif;font-weight:700;font-size:84px;color:var(--white)}
</style>
</head>
<body>

<!-- Cover -->
<section class="slide slide--dark" style="top:62px">
  <div class="cover-bg" role="img" aria-label="Background photo of engineers working in an automotive factory, tinted navy"></div>
  <svg class="cover-shape" viewBox="0 0 420 608" aria-hidden="true"><path d="M160 0 H380 Q420 0 420 60 V250 Z" fill="#2a5a86" opacity=".45"/></svg>
  <div class="brand brand--cover"><span class="brand-square"></span>Kelvanorix</div>
  <div class="cover-kicker">Welcome To</div>
  <h1 class="cover-title">KELVANORIX</h1>
  <p class="cover-sub">We Are A Company In The Manufacturing Space<br>Working Primarily In Automotive.</p>
  <div class="cover-date">July 25th ,2025</div>
</section>

<!-- About -->
<section class="slide" style="top:713px">
  <svg class="slide-header" viewBox="0 0 1080 80" aria-hidden="true"><polygon points="0,0 888,0 854,66 0,66" fill="var(--navy)"/><polygon points="902,0 1080,0 1080,64 868,64" fill="var(--orange)"/><polygon points="0,68 576,68 570,76 0,76" fill="var(--teal)"/></svg>
  <h2 class="slide-title">About Us</h2>
  <h3 class="about-lead">Sed ut perspiciatis unde omnis iste natus error sit voluptatem accusantium dolorem</h3>
  <div class="about-body">
    <p>Lorem ipsum dolor sit amet, consectetur adipiscing elit, sed do eiusmod tempor incididunt ut labore et dolore magna aliqua. Ut enim ad minim veniam, quis nostrud exercitation ullamco laboris nisi ut aliquip ex ea commodo.</p>
    <p>Duis aute irure dolor in reprehenderit in voluptate velit esse cillum dolore eu fugiat nulla pariatur. Excepteur sint occaecat cupidatat non proident, sunt in culpa qui officia deserunt mollit anim id est laborum. Sed ut perspiciatis unde omnis iste natus error sit voluptatem accusantium doloremque laudantium, totam rem aperiam, eaque ipsa quae ab illo inventore veritatis et quasi architecto beatae vitae dicta sunt explicabo.</p>
  </div>
  <div class="about-photo" role="img" aria-label="Photo of two engineers in hard hats beside a yellow industrial robot"></div>
  <svg class="slide-footer" viewBox="0 0 1080 28" aria-hidden="true"><polygon points="0,2 863,2 873,22 0,22" fill="var(--teal)"/></svg>
  <span class="footer-page">PAGE | 02</span><span class="footer-copy">© 2025 Kelvanorix | All Rights Reserved</span>
  <div class="brand brand--footer"><span class="brand-square"></span>Kelvanorix</div>
</section>

<!-- Experiences -->
<section class="slide" style="top:1365px">
  <svg class="slide-header" viewBox="0 0 1080 80" aria-hidden="true"><polygon points="0,0 888,0 854,66 0,66" fill="var(--navy)"/><polygon points="902,0 1080,0 1080,64 868,64" fill="var(--orange)"/><polygon points="0,68 576,68 570,76 0,76" fill="var(--teal)"/></svg>
  <h2 class="slide-title">Our Experiences</h2>
  <svg class="chart" viewBox="0 0 630 400" role="img" aria-label="Bar chart of weekly values">
    <g stroke="var(--grid)" stroke-width="1">
      <line x1="46" y1="13" x2="622" y2="13"/><line x1="46" y1="74" x2="622" y2="74"/><line x1="46" y1="134" x2="622" y2="134"/><line x1="46" y1="195" x2="622" y2="195"/><line x1="46" y1="256" x2="622" y2="256"/><line x1="46" y1="316" x2="622" y2="316"/>
      <line x1="46" y1="13" x2="46" y2="377"/><line x1="128" y1="13" x2="128" y2="377"/><line x1="211" y1="13" x2="211" y2="377"/><line x1="293" y1="13" x2="293" y2="377"/><line x1="375" y1="13" x2="375" y2="377"/><line x1="457" y1="13" x2="457" y2="377"/><line x1="540" y1="13" x2="540" y2="377"/><line x1="622" y1="13" x2="622" y2="377"/>
    </g>
    <line x1="46" y1="377" x2="622" y2="377" stroke="#b9bec5"/>
    <g text-anchor="end"><text x="30" y="17">120</text><text x="30" y="78">100</text><text x="30" y="138">80</text><text x="30" y="199">60</text><text x="30" y="260">40</text><text x="30" y="320">20</text><text x="30" y="381">0</text></g>
    <g fill="var(--navy)">
      <rect x="71" y="74" width="13" height="303"/><rect x="153" y="104" width="13" height="273"/><rect x="236" y="225" width="13" height="152"/><rect x="318" y="74" width="13" height="303"/><rect x="400" y="74" width="13" height="303"/><rect x="483" y="195" width="13" height="182"/><rect x="565" y="225" width="13" height="152"/>
    </g>
    <g>
      <rect x="90" y="104" width="13" height="273" fill="var(--orange)"/><rect x="172" y="134" width="13" height="243" fill="var(--teal)"/><rect x="255" y="74" width="13" height="303" fill="var(--orange)"/><rect x="337" y="195" width="13" height="182" fill="var(--teal)"/><rect x="419" y="104" width="13" height="273" fill="var(--orange)"/><rect x="502" y="150" width="13" height="227" fill="var(--teal)"/><rect x="584" y="74" width="13" height="303" fill="var(--orange)"/>
    </g>
    <g text-anchor="middle">
      <text x="77" y="66">100</text><text x="96" y="96">90</text><text x="159" y="96">90</text><text x="178" y="126">80</text><text x="242" y="217">50</text><text x="261" y="66">100</text><text x="324" y="66">100</text><text x="343" y="187">60</text><text x="406" y="66">100</text><text x="425" y="96">90</text><text x="489" y="187">60</text><text x="508" y="142">75</text><text x="571" y="217">50</text><text x="590" y="66">100</text>
      <text x="87" y="395">Sun</text><text x="169" y="395">Mon</text><text x="252" y="395">Tue</text><text x="334" y="395">Wed</text><text x="416" y="395">Thu</text><text x="499" y="395">Fri</text><text x="581" y="395">Sat</text>
    </g>
  </svg>
  <ul class="tick-list">
    <li><svg viewBox="0 0 14 14"><circle cx="7" cy="7" r="7" fill="var(--orange)"/><path d="M4 7.2 6.1 9.2 10 5" fill="none" stroke="#fff" stroke-width="1.6"/></svg>Lorem ipsum dolor sit consectetur adipiscing elit, sed do eiusmod tempor incididunt ut labore et dolore</li>
    <li><svg viewBox="0 0 14 14"><circle cx="7" cy="7" r="7" fill="var(--orange)"/><path d="M4 7.2 6.1 9.2 10 5" fill="none" stroke="#fff" stroke-width="1.6"/></svg>Lorem ipsum dolor sit consectetur adipiscing elit, sed do eiusmod</li>
    <li><svg viewBox="0 0 14 14"><circle cx="7" cy="7" r="7" fill="var(--orange)"/><path d="M4 7.2 6.1 9.2 10 5" fill="none" stroke="#fff" stroke-width="1.6"/></svg>Lorem ipsum dolor sit consectetur adipiscing elit, sed do eiusmod tempor incididunt ut labore et dolore</li>
    <li><svg viewBox="0 0 14 14"><circle cx="7" cy="7" r="7" fill="var(--orange)"/><path d="M4 7.2 6.1 9.2 10 5" fill="none" stroke="#fff" stroke-width="1.6"/></svg>Lorem ipsum dolor sit consectetur adipiscing elit, sed do eiusmod</li>
    <li><svg viewBox="0 0 14 14"><circle cx="7" cy="7" r="7" fill="var(--orange)"/><path d="M4 7.2 6.1 9.2 10 5" fill="none" stroke="#fff" stroke-width="1.6"/></svg>Lorem ipsum dolor sit consectetur adipiscing elit, sed do eiusmod tempor incididunt ut labore et dolore</li>
    <li><svg viewBox="0 0 14 14"><circle cx="7" cy="7" r="7" fill="var(--orange)"/><path d="M4 7.2 6.1 9.2 10 5" fill="none" stroke="#fff" stroke-width="1.6"/></svg>Lorem ipsum dolor sit consectetur adipiscing elit, sed do eiusmod</li>
  </ul>
  <svg class="slide-footer" viewBox="0 0 1080 28" aria-hidden="true"><polygon points="0,2 863,2 873,22 0,22" fill="var(--teal)"/></svg>
  <span class="footer-page">PAGE | 03</span><span class="footer-copy">© 2025 Kelvanorix | All Rights Reserved</span>
  <div class="brand brand--footer"><span class="brand-square"></span>Kelvanorix</div>
</section>

<!-- Services -->
<section class="slide" style="top:2017px">
  <svg class="slide-header" viewBox="0 0 1080 80" aria-hidden="true"><polygon points="0,0 888,0 854,66 0,66" fill="var(--navy)"/><polygon points="902,0 1080,0 1080,64 868,64" fill="var(--orange)"/><polygon points="0,68 576,68 570,76 0,76" fill="var(--teal)"/></svg>
  <h2 class="slide-title">Our Services</h2>
  <article class="service-card" style="left:53px">
    <div class="service-photo" role="img" aria-label="Photo of two engineers in safety vests reviewing plans on a site" style="background:linear-gradient(160deg,#5f7f9c,#3b4a3a 55%,#c7c84a)"></div>
    <div class="service-kicker">Service 01</div>
    <h3 class="service-name">Sed ut perspiciatis</h3>
    <p class="service-text">Lorem ipsum dolor sit amet, consectetur adipiscing elit, sed do eiusmod tempor incididunt ut labore et dolore magna aliqua. Ut enim ad minim veniam, quis nostrud</p>
  </article>
  <article class="service-card" style="left:384px">
    <div class="service-photo" role="img" aria-label="Photo of a technician with a tablet beside a robotic arm" style="background:linear-gradient(150deg,#2f4a6a,#1f3552 50%,#8d98a6)"></div>
    <div class="service-kicker">Service 02</div>
    <h3 class="service-name">Sed ut perspiciatis unde</h3>
    <p class="service-text">Lorem ipsum dolor sit amet, consectetur adipiscing elit, sed do eiusmod tempor incididunt ut labore et dolore magna aliqua. Ut enim ad minim veniam, quis nostrud</p>
  </article>
  <article class="service-card" style="left:717px">
    <div class="service-photo" role="img" aria-label="Photo of a machined metal part resting on technical drawings" style="background:linear-gradient(150deg,#6b747e,#b8bec4 50%,#d9dcdf)"></div>
    <div class="service-kicker">Service 03</div>
    <h3 class="service-name">Sed ut perspiciatis unde</h3>
    <p class="service-text">Lorem ipsum dolor sit amet, consectetur adipiscing elit, sed do eiusmod tempor incididunt ut labore et dolore magna aliqua. Ut enim ad minim veniam, quis nostrud</p>
  </article>
  <svg class="slide-footer" viewBox="0 0 1080 28" aria-hidden="true"><polygon points="0,2 863,2 873,22 0,22" fill="var(--teal)"/></svg>
  <span class="footer-page">PAGE | 04</span><span class="footer-copy">© 2025 Kelvanorix | All Rights Reserved</span>
  <div class="brand brand--footer"><span class="brand-square"></span>Kelvanorix</div>
</section>

<!-- Blank content -->
<section class="slide" style="top:2668px">
  <svg class="slide-header" viewBox="0 0 1080 80" aria-hidden="true"><polygon points="0,0 888,0 854,66 0,66" fill="var(--navy)"/><polygon points="902,0 1080,0 1080,64 868,64" fill="var(--orange)"/><polygon points="0,68 576,68 570,76 0,76" fill="var(--teal)"/></svg>
  <h2 class="slide-title">Titile Goes Here</h2>
  <svg class="slide-footer" viewBox="0 0 1080 28" aria-hidden="true"><polygon points="0,2 863,2 873,22 0,22" fill="var(--teal)"/></svg>
  <span class="footer-page">PAGE | 05</span><span class="footer-copy">© 2025 Kelvanorix | All Rights Reserved</span>
  <div class="brand brand--footer"><span class="brand-square"></span>Kelvanorix</div>
</section>

<!-- Team -->
<section class="slide" style="top:3320px">
  <svg class="slide-header" viewBox="0 0 1080 80" aria-hidden="true"><polygon points="0,0 888,0 854,66 0,66" fill="var(--navy)"/><polygon points="902,0 1080,0 1080,64 868,64" fill="var(--orange)"/><polygon points="0,68 576,68 570,76 0,76" fill="var(--teal)"/></svg>
  <h2 class="slide-title">Meet The Team</h2>
  <article class="member member--top" style="left:47px"><div style="padding:74px 30px 0"><div class="member-name">Rhea Castell</div><div class="member-role">Sed ut perspiciatis unde</div><p class="member-text">Lorem ipsum dolor sit amet, consectetur adipiscing elit, sed do eiusmod tempor incididunt ut labore et dolore</p></div></article>
  <article class="member member--top" style="left:384px"><div style="padding:74px 30px 0"><div class="member-name">Nolan Ferris</div><div class="member-role">Sed ut perspiciatis unde</div><p class="member-text">Lorem ipsum dolor sit amet, consectetur adipiscing elit, sed do eiusmod tempor incididunt ut labore et dolore</p></div></article>
  <article class="member member--top" style="left:718px"><div style="padding:74px 30px 0"><div class="member-name">Ivo Brandt</div><div class="member-role">Sed ut perspiciatis unde</div><p class="member-text">Lorem ipsum dolor sit amet, consectetur adipiscing elit, sed do eiusmod tempor incididunt ut labore et dolore</p></div></article>
  <div class="avatar" role="img" aria-label="Team member portrait" style="left:160px;top:116px;width:88px;height:88px"></div>
  <div class="avatar" role="img" aria-label="Team member portrait" style="left:497px;top:116px;width:88px;height:88px"></div>
  <div class="avatar" role="img" aria-label="Team member portrait" style="left:831px;top:116px;width:88px;height:88px"></div>
  <article class="member member--wide" style="left:84px"><div style="padding:24px 24px 0 68px"><div class="member-name">Talia Morrow</div><div class="member-role">Sed ut perspiciatis unde</div><p class="member-text">Lorem ipsum dolor sit amet, consectetur adipiscing elit, sed do eiusmod tempor incididunt ut labore et dolore magna aliqua. Ut enim ad minim veniam.</p></div></article>
  <article class="member member--wide" style="left:593px"><div style="padding:24px 20px 0 67px"><div class="member-name">Lena Quist</div><div class="member-role">Sed ut perspiciatis unde</div><p class="member-text">Lorem ipsum dolor sit amet, consectetur adipiscing elit, sed do eiusmod tempor incididunt ut labore et dolore magna aliqua, Ut enim ad minim veniam, quis nostrud.</p></div></article>
  <div class="avatar" role="img" aria-label="Team member portrait" style="left:45px;top:418px;width:90px;height:90px"></div>
  <div class="avatar" role="img" aria-label="Team member portrait" style="left:555px;top:418px;width:90px;height:90px"></div>
  <svg class="slide-footer" viewBox="0 0 1080 28" aria-hidden="true"><polygon points="0,2 863,2 873,22 0,22" fill="var(--teal)"/></svg>
  <span class="footer-page">PAGE | 06</span><span class="footer-copy">© 2025 Kelvanorix | All Rights Reserved</span>
  <div class="brand brand--footer"><span class="brand-square"></span>Kelvanorix</div>
</section>

<!-- Q&A -->
<section class="slide" style="top:3972px">
  <svg class="slide-header" viewBox="0 0 1080 80" aria-hidden="true"><polygon points="0,0 888,0 854,66 0,66" fill="var(--navy)"/><polygon points="902,0 1080,0 1080,64 868,64" fill="var(--orange)"/><polygon points="0,68 576,68 570,76 0,76" fill="var(--teal)"/></svg>
  <h2 class="slide-title">Questions &amp; Answers</h2>
  <div class="qa-art" role="img" aria-label="Illustration of two speech bubbles reading Q and A"></div>
  <svg class="slide-footer" viewBox="0 0 1080 28" aria-hidden="true"><polygon points="0,2 863,2 873,22 0,22" fill="var(--teal)"/></svg>
  <span class="footer-page">PAGE | 07</span><span class="footer-copy">© 2025 Kelvanorix | All Rights Reserved</span>
  <div class="brand brand--footer"><span class="brand-square"></span>Kelvanorix</div>
</section>

<!-- Thank you -->
<section class="slide slide--dark" style="top:4626px">
  <div class="cover-bg" role="img" aria-label="Faint background photo of a handshake, tinted navy" style="background:linear-gradient(180deg,#0f2e52,#0a2240)"></div>
  <div class="brand brand--thanks"><span class="brand-square"></span>Kelvanorix</div>
  <h2 class="thanks-title">THANKING YOU!</h2>
</section>

</body>
</html>
```